Visual design for database driven web application

Need a clean, professional looking visual design for a web application.

PLUME is the new standardized K-12 school testing program for the state of Texas. We are building an application named PLUME-Finder (clever, yeah?) that will allow teachers, school administrators, and others to EASILY sort through millions of records of student data and print or export reports showing just the information they need about their students.

The state currently doesn't provide a user-friendly way to do this. They provide a "data dump" spreadsheet that school administrators and teachers must figure out how to manipulate to get the data they need. We are building a Web-based tool that will make it super simple and easy for our users to get the data they need in a format that works for them.

I've created a basic wireframe of the main application screen in Vellum QD Max. I need you to "skin" the wireframe to make it look good. Your mockup will set the tone for branding and visual design throughout the site.

See the attached screenshots. There are a few variations of the screen that include dynamic panels that open & close. Start by designing just the main screen and if you have time, do one or two of the panels. Thanks!
Updates

Target Market(s)

K-12 education professionals (teachers, administrators) in the state of Texas

Industry/Entity Type

Building

Requirements
Must have
• Your mockups should include all of the features & content shown in the attached screenshots.

However, you don't have to show all 10 rows of data. You can just do the column headers and one row of data. (It would be repetitive and unnecessary to spend time re-creating the entire grid with all of that data just to show your visual styling.)

The design should reflect the following concepts:

- Texas
- Education
- Simplicity
- Helpfulness
- Trust
- Professionalism

If I select your design, I will want your design source files (Illustrator, Photoshop, etc.)
Nice to have
• A logo in the upper left corner for PLUME-Finder. The logo should definitely communicate the design concepts described under "must have."

```html
<!DOCTYPE html>
<html lang="en">
<head>
<meta charset="utf-8">
<title>PLUME-Finder – Home</title>
<link rel="stylesheet" href="https://fonts.googleapis.com/css2?family=Noto+Sans:wght@400;700&display=swap">
<style>
:root{
  --night:#131758;
  --night-deep:#0b0e3e;
  --header-top:#0d1560;
  --header-bottom:#2a3c9e;
  --panel-top:#27318a;
  --art-fill:#222c80;
  --red:#d8242a;
  --red-dark:#8a0e12;
  --gold:#f2e21c;
  --orange:#ef9a10;
  --white:#ffffff;
  --field:#8e91b3;
  --field-dim:#6f7295;
  --field-edge:#0a0c2a;
  --green:#9fe06a;
  --panel-edge:#070926;
}
*{box-sizing:border-box;margin:0;padding:0}
html,body{width:1200px;height:734px;overflow:hidden}
body{background:var(--night);font-family:"Noto Sans",sans-serif;color:var(--white);position:relative}

.masthead{position:absolute;left:0;top:0;width:1200px;height:126px;
  background:linear-gradient(180deg,var(--header-top) 0%,var(--header-bottom) 100%)}
.brand{position:absolute;left:34px;top:26px;font-size:64px;font-weight:700;color:var(--orange);line-height:1}
.crowd{position:absolute;left:520px;top:10px;width:190px;height:94px;background:var(--art-fill)}
.userbar{position:absolute;left:763px;top:15px;width:412px;height:36px;background:var(--night-deep);
  border:2px solid #05061c;display:flex;align-items:center;padding:0 14px 0 8px;font-size:17px}
.userbar .greet{color:var(--gold);font-weight:700;flex:1}
.userbar a{color:var(--white);text-decoration:none}
.userbar .sep{margin:0 10px;font-weight:700}
.search{position:absolute;left:763px;top:87px;display:flex;align-items:flex-end}
.search input{width:206px;height:32px;background:var(--field);border:2px solid var(--field-edge);
  font:17px "Noto Sans",sans-serif;color:#3a3c60;padding-left:8px}
.search .go{width:64px;height:32px;border:2px solid var(--field-edge);background:linear-gradient(180deg,#9a9dbd,#6f7399)}
.search .options{margin-left:10px;font-size:17px;line-height:1;margin-bottom:2px}

.rule{position:absolute;left:26px;top:126px;width:1174px;height:10px;background:var(--red)}
.tabs{position:absolute;left:34px;top:138px;display:flex;gap:2px}
.tab{height:31px;padding:0 18px;display:flex;align-items:center;font-size:17px;background:var(--red);
  color:var(--white);transform:skewX(-12deg);border:2px solid var(--red-dark)}
.tab span{transform:skewX(12deg)}
.tab.active{background:var(--white);color:#000;border-color:var(--red)}
.stamp{position:absolute;right:28px;top:146px;font-size:12px}

.panel{position:absolute;top:183px;height:505px;border-radius:70px;border:3px solid var(--panel-edge);
  background:linear-gradient(180deg,var(--panel-top) 0%,var(--night-deep) 100%);
  box-shadow:0 0 14px rgba(0,0,0,.6)}
.intro{left:40px;width:688px}
.intro h1{position:absolute;left:64px;top:26px;font-size:29px;font-weight:400;color:var(--gold)}
.intro .copy{position:absolute;left:55px;top:70px;font-size:18px;line-height:24px;letter-spacing:.3px}
.intro .copy p{margin-bottom:24px}
.intro .copy .p1{width:440px}
.intro .copy .p2{width:460px}
.intro .copy .p3{width:505px}
.scope{position:absolute;left:470px;top:100px;width:190px;height:265px;background:var(--art-fill)}

.signup{left:748px;width:414px}
.signup .lead{position:absolute;left:0;right:0;top:8px;text-align:center;color:var(--orange);font-size:29px;line-height:36px}
.signup .lead .name{display:block;font-weight:700;font-size:34px;line-height:38px}
.form{position:absolute;left:10px;top:132px}
.row{display:flex;align-items:center;height:44.6px}
.row label{width:175px;text-align:right;font-size:21px;padding-right:4px}
.row input{width:205px;height:32px;background:linear-gradient(90deg,var(--field-dim),var(--field));border:2px solid var(--field-edge)}
.submit{position:absolute;left:238px;top:400px;width:138px;height:49px;border:3px solid #1d2a9c;
  background:linear-gradient(180deg,#d8f7a0,var(--green) 50%,#6cc83a);font:34px "Noto Sans",sans-serif;color:#000}

.footer{position:absolute;left:428px;top:710px;font-size:10px;color:var(--gold)}
.footer a{color:var(--gold);text-decoration:none}
.footer .links{margin-left:36px}
</style>
</head>
<body>
<header class="masthead">
  <div class="brand">PLUME-Finder</div>
  <div class="crowd" role="img" aria-label="Silhouettes of cheering students"></div>
  <div class="userbar"><span class="greet">Welcome, Dana</span><a href="#">my profile</a><span class="sep">/</span><a href="#">log out</a></div>
  <form class="search">
    <input type="text" placeholder="Quick Search">
    <button class="go" type="button" aria-label="Search"></button>
    <span class="options">search options</span>
  </form>
</header>
<div class="rule"></div>
<nav class="tabs">
  <a class="tab active"><span>Home</span></a>
  <a class="tab"><span>Instructions</span></a>
  <a class="tab"><span>Student Data</span></a>
</nav>
<div class="stamp">11/30/2011&nbsp;&nbsp;&nbsp;1:51 pm CST</div>

<section class="panel intro">
  <h1>Welcome to PLUME-Finder!</h1>
  <div class="scope" role="img" aria-label="Silhouette of a telescope on a tripod"></div>
  <div class="copy">
    <p class="p1">Lorem ipsum dolor sit amet, consectetur adipiscing elit. Quisque ornare consequat libero, vitae dictum nisl lobortis eget. Quisque sit amet lacinia leo. Maecenas vel ligula id lacus gravida lobortis.</p>
    <p class="p2">Vivamus posuere laoreet est eu egestas. Sed lacinia pharetra lacus, et ullamcorper mauris vehicula eu. Quisque eget velit nunc, nec porttitor arcu.</p>
    <p class="p3">Aenean suscipit erat in nisl blandit commodo. Integer justo eros, ornare eu condimentum eu, venenatis eu nunc. Vestibulum convallis, eros quis suscipit suscipit, velit ante commodo neque, a rutrum risus ipsum sed ipsum. Nulla facilisi.</p>
  </div>
</section>

<section class="panel signup">
  <div class="lead">Register with<span class="name">PLUME-Finder</span>Begin searching today!</div>
  <form class="form">
    <div class="row"><label>Name</label><input type="text"></div>
    <div class="row"><label>E-mail</label><input type="email"></div>
    <div class="row"><label>Educator ID#</label><input type="text"></div>
    <div class="row"><label>School District</label><input type="text"></div>
    <div class="row"><label>Password</label><input type="password"></div>
    <div class="row"><label>Verify Password</label><input type="password"></div>
  </form>
  <button class="submit" type="button">Submit</button>
</section>

<footer class="footer">Copyright © 2012&nbsp; PLUME-Finder<span class="links"><a href="#">Terms of Use</a> &nbsp;/&nbsp; <a href="#">Privacy Policy</a> &nbsp;/&nbsp; <a href="#">Contact Us</a></span></footer>
</body>
</html>
```